Design business cards for Ironvale Barbers (Opening March so won't need finalised till January2018

Ironvale Barbers is the new age barbers and skincare for all men. Creating tailor made haircuts & customised skincare solutions for the perfect healthy manly look. The Barbers will have a industrial, rustic, worldly feel about it. Rustic red brick wall with old wine barrels as the work stations with the old fashion barber chairs. Concrete floor and a bit corrugated iron around.
Target Market(s)
Professional males who like a great haircut, wet shave and may consider a facial if in the right environment. Total pampering experience in a boys environment.
Industry/Entity Type
Barber
Contact Information for Business Card
Front- Logo - address is 42 Kowhai Rd Taupo
Ph - (07) 548 9163
www.ironvalebarbers.com
email - hello@ironvale.co.nz
Back of card
Mens Haircare - Wet Shaving - Facials - Skin Prescriptions
We are doing a loyalty program - 6 squares numbered then 7th free
Colors
Designer to choose colors to be used in the design.
Requirements
Must have
- Clean simple easy to read.
Nice to have
- Our current colours are white font on black background but thinking we need to introduce another colour. Maybe white logo on a copper, bronze or rusty background. Or even a rustic red brick wall with white writing. Want it clean simple to read. Maybe a burgundy?
Should not have
- no images like heads, scissors, razors please

```html
<!DOCTYPE html>
<html lang="en">
<head>
<meta charset="utf-8">
<title>Ironvale Barbers – Business Cards</title>
<link rel="stylesheet" href="https://fonts.googleapis.com/css2?family=Roboto:wght@400;700;900&display=swap">
<style>
  :root {
    --crimson: #c41e2e;
    --crimson-deep: #a8121f;
    --crimson-light: #d9303f;
    --ink: #0b0b0b;
    --paper: #ffffff;
    --paper-shade: #ececec;
    --backdrop: #e6e4e1;
    --text-font: "Roboto", Arial, sans-serif;
  }
  * { box-sizing: border-box; margin: 0; padding: 0; }
  html, body { width: 1200px; height: 675px; overflow: hidden; }
  body { background: var(--backdrop); font-family: var(--text-font); position: relative; }

  .card {
    position: absolute;
    top: 188px;
    width: 520px;
    height: 298px;
    overflow: hidden;
    box-shadow: 0 10px 28px rgba(0,0,0,0.22);
  }

  .brand-name {
    font-family: var(--text-font);
    font-weight: 900;
    text-transform: uppercase;
    letter-spacing: 2px;
    line-height: 1.05;
  }
  .brand-name__line { display: block; }

  /* Appointment card (front, red) */
  .card--appointment { left: 60px; background: var(--paper); }
  .appointment__head {
    height: 214px;
    background: linear-gradient(160deg, var(--crimson-light), var(--crimson-deep));
    display: flex; align-items: center; justify-content: center;
    text-align: center;
  }
  .appointment__head .brand-name { color: var(--paper); font-size: 50px; }
  .appointment__foot {
    padding: 10px 22px 0;
    color: var(--crimson);
    font-weight: 700;
  }
  .services { font-size: 14.5px; letter-spacing: 0.8px; white-space: nowrap; }
  .booking { display: flex; gap: 14px; margin-top: 14px; font-size: 14.5px; letter-spacing: 0.8px; }
  .booking__field { display: flex; align-items: flex-end; flex: 1; gap: 6px; }
  .booking__line { flex: 1; border-bottom: 1.5px dashed var(--crimson); margin-bottom: 3px; }

  /* Contact card (back, white / black) */
  .card--contact { left: 620px; background: linear-gradient(120deg, var(--paper), var(--paper-shade)); }
  .contact__panels { position: absolute; inset: 0; }
  .contact__brand { position: absolute; left: 34px; top: 104px; width: 220px; text-align: center; }
  .contact__brand .brand-name { color: var(--crimson); font-size: 34px; }
  .contact__person { position: absolute; left: 356px; top: 44px; color: var(--paper); }
  .person__name { font-size: 16px; font-weight: 700; letter-spacing: 0.5px; }
  .person__role { font-size: 7px; letter-spacing: 0.6px; text-transform: uppercase; margin-top: 2px; }
  .contact__list { position: absolute; left: 306px; top: 118px; list-style: none; }
  .contact__item {
    display: flex; align-items: center; gap: 10px;
    color: var(--crimson); font-size: 13px; letter-spacing: 0.6px;
    height: 38px; white-space: nowrap;
  }
  .contact__item:nth-child(2) { margin-left: -10px; }
  .contact__item:nth-child(3) { margin-left: -20px; }
  .contact__item:nth-child(4) { margin-left: -30px; }
  .contact__icon {
    width: 24px; height: 24px; border-radius: 50%;
    background: var(--paper);
    display: flex; align-items: center; justify-content: center;
    flex: none;
  }
  .contact__icon svg { width: 14px; height: 14px; }
</style>
</head>
<body>

  <section class="card card--appointment" aria-label="Appointment card">
    <div class="appointment__head">
      <h1 class="brand-name"><span class="brand-name__line">Ironvale</span><span class="brand-name__line">Barbers</span></h1>
    </div>
    <div class="appointment__foot">
      <p class="services">Mens Haircare - Wet Shaving - Facials - Skin Prescriptions</p>
      <div class="booking">
        <div class="booking__field"><span>Date -</span><span class="booking__line"></span></div>
        <div class="booking__field"><span>Time -</span><span class="booking__line"></span></div>
      </div>
    </div>
  </section>

  <section class="card card--contact" aria-label="Contact card">
    <svg class="contact__panels" width="520" height="298" viewBox="0 0 520 298" aria-hidden="true">
      <polygon points="330,0 520,0 520,298 250,298" fill="var(--ink)"/>
      <polygon points="318,34 520,34 520,88 300,88" fill="var(--crimson)"/>
      <polygon points="318,34 335,34 317,88 300,88" fill="var(--crimson-deep)"/>
    </svg>

    <div class="contact__brand">
      <h2 class="brand-name"><span class="brand-name__line">Ironvale</span><span class="brand-name__line">Barbers</span></h2>
    </div>

    <div class="contact__person">
      <p class="person__name">NAME</p>
      <p class="person__role">Designation</p>
    </div>

    <ul class="contact__list">
      <li class="contact__item">
        <span class="contact__icon">
          <svg viewBox="0 0 24 24" fill="none" stroke="var(--crimson)" stroke-width="2" stroke-linecap="round" stroke-linejoin="round"><path d="M5 3h4l2 5-3 2a12 12 0 0 0 6 6l2-3 5 2v4a2 2 0 0 1-2 2A17 17 0 0 1 3 5a2 2 0 0 1 2-2z"/></svg>
        </span>
        (07) 548 9163
      </li>
      <li class="contact__item">
        <span class="contact__icon">
          <svg viewBox="0 0 24 24" fill="none" stroke="var(--crimson)" stroke-width="2" stroke-linejoin="round"><rect x="3" y="6" width="18" height="12" rx="1"/><path d="M3 7l9 6 9-6"/></svg>
        </span>
        hello@ironvale.co.nz
      </li>
      <li class="contact__item">
        <span class="contact__icon">
          <svg viewBox="0 0 24 24" fill="none" stroke="var(--crimson)" stroke-width="2"><circle cx="12" cy="12" r="9"/><path d="M3 12h18M12 3c3 3 3 15 0 18M12 3c-3 3-3 15 0 18"/></svg>
        </span>
        www.ironvalebarbers.com
      </li>
      <li class="contact__item">
        <span class="contact__icon">
          <svg viewBox="0 0 24 24" fill="none" stroke="var(--crimson)" stroke-width="2" stroke-linejoin="round"><path d="M12 22s7-7 7-12a7 7 0 0 0-14 0c0 5 7 12 7 12z"/><circle cx="12" cy="10" r="2.5"/></svg>
        </span>
        42 Kowhai Rd Taupo
      </li>
    </ul>
  </section>

</body>
</html>
```